VORLEN Website Design

We need a website designed for our company VORLEN. We are a luxury lifestyle club that will provide benefits and services for our members. The site should be clean & sleek, preferably using black and white (or darker colors). (example sites: brimvale.example, tusko.example)

Here is a link of a sample page I did using wix. (https://pelmundry4.sitebuild.example/mypage) This can be used to get a general idea.

Target Market(s)

Upper Middle Class in the United States

Number of Pages Required

5+ page

Font styles to use
Sans Serif
Other font styles liked:
• Arial (or other similar fonts)

Requirements
Must have
• A clean design that is eye-catching and speaks to our company.
Nice to have
• Ideas for copy.

```html
<!DOCTYPE html>
<html lang="en">
<head>
<meta charset="utf-8">
<title>VORLEN — A Members Only Lifestyle Club</title>
<link rel="stylesheet" href="https://fonts.googleapis.com/css2?family=Nunito+Sans:ital,wght@0,300;0,400;0,600;1,300&display=swap">
<style>
:root{
  --ink:#000;
  --paper:#fff;
  --muted:#bdbdbd;
  --rule:#8a8a8a;
  --field:#111;
}
*{margin:0;padding:0;box-sizing:border-box}
html,body{width:690px;height:1200px;overflow:hidden;background:var(--ink)}
body{font-family:"Nunito Sans",Arial,sans-serif;font-weight:300;color:var(--paper);position:relative}
.site-header{position:absolute;left:0;top:0;width:690px;height:25px;background:var(--paper);color:var(--ink)}
.brand{position:absolute;left:10px;top:5px;font-size:12px;font-weight:400;letter-spacing:.5px}
.main-nav{position:absolute;right:10px;top:8px;display:flex;gap:14px;font-size:4.5px;font-weight:400;letter-spacing:.2px}
.main-nav a{color:var(--ink);text-decoration:none;padding:2px 4px;position:relative}
.main-nav a.is-active{background:var(--ink);color:var(--paper)}
.main-nav a.is-active::after{content:"";position:absolute;left:50%;top:12px;margin-left:-4px;border:4px solid transparent;border-top-color:var(--ink)}
.header-bar{position:absolute;left:0;top:25px;width:690px;height:5px;background:var(--ink)}
.hero{position:absolute;left:0;top:30px;width:690px;height:299px;background:radial-gradient(ellipse at 60% 40%,#c69a6a 0%,#7a4f33 35%,#3a2a22 65%,#1d1613 100%)}
.hero-title{position:absolute;left:0;right:0;top:128px;text-align:center;font-size:27px;font-weight:300;color:var(--paper)}
.hero-arrow{position:absolute;right:12px;top:142px}
.hero-dots{position:absolute;left:333px;top:282px;display:flex;gap:6px}
.hero-dots span{width:5px;height:5px;border-radius:50%;background:rgba(255,255,255,.55)}
.quote-band{position:absolute;left:0;top:329px;width:690px;height:58px;text-align:center}
.quote-text{margin-top:15px;font-size:9.5px;font-style:italic}
.quote-text b{font-size:14px;font-weight:600;font-style:normal;vertical-align:-2px}
.quote-author{font-size:8.5px;font-style:italic;margin-top:1px}
.title-band{position:absolute;left:0;top:388px;width:690px;height:35px;background:var(--paper);color:var(--ink);text-align:center;font-size:19px;font-style:italic;line-height:35px}
.feature-text{position:absolute;width:200px;text-align:center;font-size:8.4px;line-height:14.4px}
.feature-text svg{display:block;margin:0 auto 4px}
.feature-title{font-size:17px;font-weight:400;line-height:20px;margin-bottom:10px;letter-spacing:.2px}
.feature-text p{margin-bottom:11px;line-height:11px}
.feature-text.about p{line-height:14.4px}
.feature-rule{width:98px;height:1px;background:var(--rule);margin:14px auto 0}
.feature-photo{position:absolute;width:378px;height:180px;border-bottom:2px solid var(--paper)}
.photo-pool{left:262px;top:447px;background:linear-gradient(160deg,#3f6b3a 0%,#6f9a5a 35%,#5fb3c8 60%,#c9b8a0 100%)}
.photo-yacht{left:51px;top:663px;background:linear-gradient(180deg,#4f7fbf 0%,#9bbce0 40%,#e8edf2 55%,#2a4f86 80%,#1c3a66 100%)}
.photo-ridge{left:262px;top:879px;background:linear-gradient(180deg,#f4e7c4 0%,#d9b96a 35%,#8a8a3a 65%,#4d5a24 100%)}
.site-footer{position:absolute;left:0;top:1128px;width:690px;height:72px;border-top:1px solid var(--rule);font-size:5px;font-weight:400}
.footer-brand{position:absolute;left:111px;top:20px;text-align:center;font-size:11px}
.footer-brand small{display:block;font-size:3.5px;margin-top:6px}
.footer-col{position:absolute;top:21px;line-height:8.6px}
.footer-col.links{left:183px}
.footer-col.social{left:255px}
.footer-col.social span{display:inline-block;width:5px;height:5px;border-radius:50%;background:var(--paper);margin-right:7px;vertical-align:-1px}
.newsletter{position:absolute;left:328px;top:22px}
.newsletter-form{display:flex;margin-top:8px}
.newsletter-field{width:75px;height:14px;border:1px solid var(--paper);background:var(--field);color:var(--paper);font-size:4px;line-height:12px;padding-left:7px}
.newsletter-btn{width:22px;height:14px;background:var(--paper);color:var(--ink);font-size:4px;line-height:14px;text-align:center}
.footer-col.contact{left:509px;top:20px;line-height:7.3px;font-size:4.5px}
</style>
</head>
<body>
<header class="site-header">
  <div class="brand">VORLEN</div>
  <nav class="main-nav">
    <a class="is-active">HOME</a><a>ABOUT</a><a>SERVICES &amp; BENEFITS</a><a>APPLY</a><a>CONTACT</a>
  </nav>
</header>
<div class="header-bar"></div>

<section class="hero" role="img" aria-label="Guests in evening wear sharing wine and cigars at a private lounge">
  <h1 class="hero-title">A Members Only Lifestyle Club</h1>
  <svg class="hero-arrow" width="10" height="16" viewBox="0 0 10 16"><path d="M2 2l6 6-6 6" fill="none" stroke="#d8d8d8" stroke-width="2"/></svg>
  <div class="hero-dots"><span></span><span></span><span></span></div>
</section>

<section class="quote-band">
  <p class="quote-text"><b>“</b> I don’t have dreams, I have goals <b>”</b></p>
  <p class="quote-author">- Marcus Dalen -</p>
</section>

<div class="title-band">A Members Only Lifestyle Club</div>

<article class="feature-text about" style="left:36px;top:452px">
  <svg width="16" height="16" viewBox="0 0 16 16"><circle cx="8" cy="8" r="7" fill="none" stroke="#fff" stroke-width="1.3"/><circle cx="8" cy="4.8" r="1" fill="#fff"/><path d="M8 7v5" stroke="#fff" stroke-width="1.4"/></svg>
  <h2 class="feature-title">ABOUT VORLEN</h2>
  <p>VORLEN is a members only lifestyle club founded in order to bring the best services, experiences, and opportunities to our diverse community of members. Our members consist of creatives, athletes, artists, and other professionals.</p>
  <div class="feature-rule"></div>
</article>
<div class="feature-photo photo-pool" role="img" aria-label="Member relaxing by a resort pool with a tablet"></div>

<div class="feature-photo photo-yacht" role="img" aria-label="Luxury yacht moored at a dock"></div>
<article class="feature-text" style="left:454px;top:663px">
  <svg width="12" height="16" viewBox="0 0 12 16"><path d="M1 2h10L6 8z M6 8v6 M3 14.5h6" fill="none" stroke="#fff" stroke-width="1.2"/></svg>
  <h2 class="feature-title">BENEFITS&amp;SERVICES</h2>
  <p>VORLEN membership provides you with amazing benefits and services. Members receive access to the best accountants, attorneys, real estate agents, private bankers/advisers and more.</p>
  <p>VORLEN members also receive access to private flight travel, premium luxury gym memberships, private social clubs, and private investment opportunities.</p>
  <div class="feature-rule" style="margin-top:3px"></div>
</article>

<article class="feature-text" style="left:36px;top:880px">
  <svg width="16" height="16" viewBox="0 0 16 16"><circle cx="8" cy="8" r="4.5" fill="none" stroke="#fff" stroke-width="1.2"/><circle cx="8" cy="8" r="1.3" fill="#fff"/><path d="M8 1v14M1 8h14M3 3l10 10M13 3L3 13" stroke="#fff" stroke-width="1"/></svg>
  <h2 class="feature-title">EXPERIENCES</h2>
  <p>VORLEN organizes and supports a ton of private events and parties for our members.</p>
  <p>Members are also provided access to exclusive venues and events from our partners.</p>
  <div class="feature-rule" style="margin-top:3px"></div>
</article>
<div class="feature-photo photo-ridge" role="img" aria-label="Hiker walking a mountain ridge at sunset"></div>

<footer class="site-footer">
  <div class="footer-brand">VORLEN<small>© VORLEN 2017</small></div>
  <div class="footer-col links">About Us<br>Contact<br>Terms &amp; Conditions</div>
  <div class="footer-col social"><span></span>Friendwall<br><span></span>Chirpline<br><span></span>Snapgram</div>
  <div class="newsletter">Subscribe to our newsletter
    <div class="newsletter-form"><div class="newsletter-field">Email Address</div><div class="newsletter-btn">OK</div></div>
  </div>
  <div class="footer-col contact">12 Linden Ct. Fairhollow, CA 90000<br>+1 555 014 2000<br>vorlenclub@mail.example</div>
</footer>
</body>
</html>
```